Kettle of Kindness Business Card Design Project

Hello, we need a business card type design as a collateral piece to be placed in hospitals and other brick and mortar locations. The name of our company is www.kettleofkindness-gifts.example and we are a gifting company that sends yummy chicken soup gift care packages across America. We have been featured on the Morning Porch Hour to the cover of Founderly magazine. We are also currently redoing a lot of our internal branding, but that going to take a few months and we don't want to wait until then, so we need a low cost solution for now.

The look and feel: We need something that is very high quality in terms of the paper stock as well as the look and feel. it needs to be simple, catchy, classy, elegant, and inexpensive to print.
We would like BOTH sides to be utilized and would like to see one version with a hole perforation to be able to potentially hang it on some sort of simple waterfall.

The other holder will be a simple, easy to use, and refill card holder that we can inexpensively place in hospitals.

CONTENT: There is not a lot of room to add things, we want it to look clean, and not busy also. Things we MUST include:
1. Kettle of Kindness / logo
2. our website and # www.kettleofkindness-gifts.example # is (877) 555-0193
3. 10% discounted code name "LADLE"

We want to grow our business in this channel and hope this will increase our awareness and people in the hospital the occasions from new baby, husbands, cancer, moms and dads, patients, surgery, will see this card and take it home to be used for a purchase.

How do we create that on this small piece?

We must tell them what we do.
"send a chicken soup care package to your loved one"

"A step beyond flowers send award winning chicken soup care packages"

A STEP BEYOND
STANDARD FLOWERS OR FRUIT BASKETS,
Kettle of Kindness sends thoughtful gifts as personal as the handwritten
sentiments that go with them. From our famous homemade soup
and baked goods to our considerate accoutrements, the package you send
is sure to be remembered. Help your organization nurture the relationships
it relies on—it’s the kind of nourishment that makes everyone feel good.

- • Ladle up the care •
Kettle of Kindness is an amiable approach to gift giving for all occasions.
Add a neighborly touch when sending sentiments like these:

-next day delivery available.

Pls review our website www.kettleofkindness-gifts.example for inspiration and ideas.

Ideas:

- We guarantee your complete satisfaction
Gift Ideas
Care Packages
Christmas Gifts
Comfort Packages
Corporate Gifts
Get Well Gifts
Hospital Gifts
Sympathy Baskets
flu gift

- as seen on the "MORNING PORCH HOUR"
- join the next generation of personal care gifts

- Our soup is made with love
- a home-style taste that even grandmas would approve of
- a portion of proceeds are donated back to the National Wellness Relief Fund
- "Gifts that just feel better"

OUR STORY:

In October 2007, I received the phone call from my mother that she had been diagnosed with Lung Cancer.

I was shocked, scared and panicked. The hardest part about hearing the news, was that she lived in New Brunswick Canada and I lived in Florida. More difficult still, I had just returned the day before from a trip visiting her. With two young children in school, I couldn't just turn around and go back.

I was so upset and felt helpless being so far away. I needed to "Do Something". I looked into sending flowers or fruit, but nothing seemed appropriate. I wanted to show her how much I cared, and in some way comfort her.

I immediately thought of chicken soup - it's what she (like many mothers) used to make to comfort me. And the idea for Kettle of Kindness was born.

Just six weeks later, I lost my mother.

During her final weeks she got lots of soup and other comforts from many of her 11 siblings and close friends. She never had the opportunity to try my soup.

However, in her honor, it is my goal to help others with sick loved ones. It is my promise to make and deliver a Kettle of Kindness to your loved ones with as much care as if I were sending it to my own mother. They'll feel better and so will you. Whether you have an ailing mother, a child away at college with the flu, or a grandchild with an ear infection, Kettle of Kindness can help you show that you care with gourmet gift baskets.

overall, we would like to have a broad use for this marketing tool so that the branding is generic, but, compelling enough to be used in a variety of locations.

Be CREATIVE!!! Have fun with it! Our brand is about comforting, care, helping, and we want it to feel warm, inviting, nostalgic, classical, vintage, unique, catchy. Not cheesy pls! We truly care about our customers and their experience with us so we want to live up to our reputation.
Updates

Reason: Hello All! I'm sorry that I haven't been able to provide feedback for ALL of your HARD WORK of which I am doing now as I was given the gift of being sick myself and have been out of work a few days. So I'm going to extend it a few days in respect to your work and getting the proper communication and feedback. thank you all!!!

Target Market(s)

hospitals, medical practices, retailers,

Industry/Entity Type

Marketing

Requirements
Should not have
• PLS DO NOT MAKE IT FEEL CHEESY, CORNY, or used car sales person feeling. look at our colors on our website and use similar WARM color choices!

```html
<!DOCTYPE html>
<html lang="en">
<head>
<meta charset="utf-8">
<title>Kettle of Kindness Business Card</title>
<link rel="stylesheet" href="https://fonts.googleapis.com/css2?family=Jost:wght@400;500;600&display=swap">
<style>
  :root {
    --backdrop: #4d3443;
    --sunny: #fccb71;
    --cream: #f4efe0;
    --plum: #4a2a3a;
  }
  * { margin: 0; padding: 0; box-sizing: border-box; }
  html, body {
    width: 1200px;
    height: 952px;
    overflow: hidden;
    background: var(--backdrop);
    font-family: "Jost", "Futura", sans-serif;
    color: var(--plum);
  }
  .stage {
    position: relative;
    width: 1200px;
    height: 952px;
  }
  .card {
    position: absolute;
    left: 200px;
    width: 800px;
    height: 400px;
    border-radius: 28px;
    overflow: hidden;
  }
  .card--front {
    top: 44px;
    background: var(--sunny);
  }
  .card--back {
    top: 508px;
    background: var(--cream);
  }

  /* Front face */
  .front-name {
    position: absolute;
    left: 0;
    right: 0;
    top: 120px;
    text-align: center;
    font-size: 64px;
    font-weight: 500;
    letter-spacing: 1px;
    line-height: 1;
  }
  .front-rule {
    position: absolute;
    left: 190px;
    right: 190px;
    top: 212px;
    height: 2px;
    background: var(--plum);
  }
  .front-url {
    position: absolute;
    left: 0;
    right: 0;
    bottom: 62px;
    text-align: center;
    font-size: 17px;
    letter-spacing: 3px;
  }

  /* Back face */
  .brand-band {
    position: absolute;
    left: 0;
    top: 92px;
    width: 345px;
    height: 128px;
    background: var(--sunny);
    display: flex;
    align-items: center;
    justify-content: center;
  }
  .brand-band__name {
    font-size: 30px;
    font-weight: 500;
    line-height: 1;
  }
  .offer {
    position: absolute;
    left: 388px;
    top: 112px;
  }
  .offer__code {
    font-size: 26px;
    font-weight: 600;
    letter-spacing: 3px;
    line-height: 1;
  }
  .offer__note {
    margin-top: 4px;
    font-size: 10px;
  }
  .contact {
    position: absolute;
    left: 388px;
    top: 206px;
    font-size: 18px;
    line-height: 1.3;
    letter-spacing: 0.5px;
  }
  .address {
    position: absolute;
    left: 48px;
    top: 300px;
    font-size: 13.5px;
    letter-spacing: 0.5px;
  }
  .edge-tab {
    position: absolute;
    right: 0;
    top: 168px;
    width: 44px;
    height: 168px;
    background: var(--sunny);
  }
</style>
</head>
<body>
<main class="stage">
  <section class="card card--front">
    <p class="front-name">Kettle of Kindness</p>
    <div class="front-rule"></div>
    <p class="front-url">www.kettleofkindness-gifts.example</p>
  </section>

  <section class="card card--back">
    <div class="brand-band">
      <p class="brand-band__name">Kettle of Kindness</p>
    </div>
    <div class="offer">
      <p class="offer__code">LADLE</p>
      <p class="offer__note">10% Discount</p>
    </div>
    <div class="contact">
      <p>(877) 555-0193</p>
      <p>www.kettleofkindness-gifts.example</p>
      <p>info@kettleofkindness-gifts.example</p>
    </div>
    <p class="address">Corporate Offices 1280 N. Larkspur Way Riverton, Ohio 45012</p>
    <div class="edge-tab"></div>
  </section>
</main>
</body>
</html>
```